Newsletter Design Project

We are looking at refreshing our corporate newsletter and general communication design.
The design will be a corporate design for our brand:
KVRB - Nordic Coach Planners Guild
For brand colours, requirements and logo look here: www.kvrb-guild.example/media
or check the attached documents.

We need to incorporate logo and brand but we are happy to refresh the palette.

Important! Attached please also find designs and colour palette of our new website-newsletter should complement these.

You are also free to use photos from events some of which can be found here:
http://www.socialpage.example/pages/Nordic-Coach-Planners-Guild/904417365290813?sk=photos_stream

We attached a sample of our newsletter. We usually include sections such as:
-CONTENTS (for navigation)
-INTRODUCTION
-NEW MEMBERS
-EVENTS
-FEATURES
-IN THE MEDIA
-ABOUT KVRB

Most important:
-PROFESSIONAL AUDIENCE-PROFESSIONAL DESIGN
-SIMPLE (see example our homepage in attachment)
-IMAGES AND GRAPHS OK
-DESIGN TO BE RE-USABLE FOR OTHER COMMUNICATIONS
-HTML format please
Updates

We are happy to increase the budget if the design is right

We have uploaded new social media icons which we would like integrated in  the design

I have uploaded a new high res version of the map that you can integrate in your designs (feel free to change colour scheme if needed)

I have also posted another Chatterly + corporate social media icon (as some mentioned it wasn't working)

Target Market(s)

B2B- audience includes various tourism companies

Industry/Entity Type

Communication

```html
<!DOCTYPE html>
<html lang="en">
<head>
<meta charset="utf-8">
<title>KVRB Newsletter</title>
<link href="https://fonts.googleapis.com/css2?family=Open+Sans:wght@400;600;700&display=swap" rel="stylesheet">
<style>
:root{
  --navy:#1b2a5e;
  --navy-deep:#131f47;
  --navy-mid:#24376f;
  --title-blue:#1f3c8c;
  --panel:#eceef2;
  --band:#d9dde6;
  --rule:#c9ced8;
  --text:#444a55;
  --muted:#6f7684;
  --white:#ffffff;
  --ring:#b8bcc4;
}
*{box-sizing:border-box;margin:0;padding:0}
html,body{width:1200px;height:2400px;overflow:hidden;background:var(--white)}
body{font-family:"Open Sans",Arial,sans-serif;color:var(--text);position:relative}
.abs{position:absolute}

.masthead{left:0;top:0;width:1200px;height:272px;background:linear-gradient(120deg,var(--navy-deep),var(--navy) 55%,var(--navy-mid))}
.masthead-map{left:380px;top:0;width:820px;height:272px;background:radial-gradient(ellipse at 70% 40%,rgba(120,150,210,.22),rgba(120,150,210,0) 65%)}
.brand{left:56px;top:0;width:264px;height:312px;background:var(--navy-deep);box-shadow:0 4px 10px rgba(0,0,0,.35);display:flex;align-items:center;justify-content:center}
.brand-ring{width:150px;height:150px;border:3px solid rgba(255,255,255,.85);border-radius:50%;display:flex;align-items:center;justify-content:center}
.brand-name{color:var(--white);font-weight:600;font-size:44px;letter-spacing:2px}
.title{left:390px;top:118px;color:var(--white);font-size:134px;font-weight:400;letter-spacing:-2px;line-height:1}
.issue{right:170px;top:268px;color:var(--title-blue);font-size:17px;font-weight:700;letter-spacing:1px}
.social{top:10px;right:12px;display:flex;gap:8px}
.social span{display:block;width:38px;height:38px;background:var(--white);opacity:.92}

.hero-photo{left:352px;top:352px;width:776px;height:240px;background:linear-gradient(180deg,#8b8f99,#5e6470 60%,#3f4550)}

.nav{left:56px;top:510px;width:264px}
.nav-cap{height:42px;background:var(--navy);clip-path:polygon(0 40%,100% 0,100% 100%,0 100%)}
.nav ul{list-style:none;margin-top:8px}
.nav li{height:40px;margin-bottom:12px;background:var(--navy);color:var(--white);font-size:16px;font-weight:600;padding-left:16px;line-height:40px;border-bottom:3px solid var(--navy-deep)}

.side-head{left:56px;width:264px;height:72px;background:var(--navy);color:var(--white);font-weight:700;font-size:24px;text-align:center;line-height:72px;box-shadow:0 3px 6px rgba(0,0,0,.3)}
.member{left:112px;width:150px;height:150px;border-radius:50%;border:15px solid var(--ring);background:#f3f4f6;display:flex;align-items:center;justify-content:center;font-size:12px;font-weight:600;color:var(--title-blue)}

.content{left:344px;top:592px;width:792px;height:1280px;background:var(--panel)}
.section h2{font-size:25px;font-weight:700;color:#222;line-height:1.2}
.section h3{font-size:25px;font-weight:700;color:var(--title-blue);line-height:1.2;margin-bottom:4px}
.section p{font-size:16px;line-height:1.4;color:var(--text)}
.more{font-size:13px;color:var(--title-blue);font-weight:600;letter-spacing:.5px;border-left:1px solid var(--rule);padding-left:8px;line-height:18px}
.rule{height:1px;background:var(--rule)}
.photo{background:linear-gradient(160deg,#9aa0aa,#5a606c)}

.events-band{left:0;top:1872px;width:1200px;height:378px;background:var(--band)}
.event-list{left:60px;top:2016px;width:260px;list-style:none}
.event-list li{margin-bottom:10px}
.event-list b{display:block;color:var(--title-blue);font-size:19px;font-weight:600;line-height:1.3}
.event-list span{font-size:14px;color:var(--muted)}
.about{left:352px;top:2160px;width:776px;height:130px;background:var(--navy);color:var(--white);padding:16px 28px}
.about h2{font-size:21px;font-weight:700;margin-bottom:6px}
.about p{font-size:13px;line-height:1.45;opacity:.92}

.footer-rule{left:40px;top:2330px;width:1120px}
.copyright{left:0;top:2342px;width:1200px;text-align:center;font-size:14px;font-weight:600;color:#333}
.follow{right:12px;top:2306px;text-align:right}
.follow small{display:block;font-size:12px;font-weight:600;margin-bottom:8px;color:#333}
.follow .icons{display:flex;gap:8px}
.follow .icons span{display:block;width:40px;height:40px;background:var(--navy)}
</style>
</head>
<body>

<header>
  <div class="abs masthead"></div>
  <div class="abs masthead-map" role="img" aria-label="Faint world map texture across the masthead"></div>
  <div class="abs brand"><div class="brand-ring"><span class="brand-name">KVRB</span></div></div>
  <h1 class="abs title">Newsletter</h1>
  <div class="abs issue">35 | MARCH</div>
  <div class="abs social" aria-label="Social links"><span></span><span></span><span></span><span></span><span></span></div>
</header>

<div class="abs hero-photo" role="img" aria-label="Photo of a conference hall with delegates seated at tables"></div>

<nav class="abs nav">
  <div class="nav-cap"></div>
  <ul>
    <li>SECTION A</li><li>SECTION B</li><li>SECTION B</li><li>SECTION B</li><li>SECTION B</li><li>SECTION B</li><li>SECTION B</li>
  </ul>
</nav>

<div class="abs side-head" style="top:924px">NEW MEMBERS</div>
<div class="abs member" style="top:1040px">LOGO</div>
<div class="abs member" style="top:1204px">LOGO</div>
<div class="abs member" style="top:1368px">LOGO</div>
<div class="abs member" style="top:1532px">LOGO</div>
<div class="abs member" style="top:1696px">LOGO</div>

<main>
  <div class="abs content"></div>

  <section class="abs section" style="left:356px;top:624px;width:772px">
    <h2>SECTION A</h2>
    <h3>ArticleTitle</h3>
    <p>Lorem ipsum dolor sit amet, consectetuer adipiscing elit. Fusce lacinia. Cras massa tortor, dignissim eu, sollicitudin eu, consequat et, magna. Proin tempor. Mauris leo orci, pretium at, pharetra a, egestas id, ligula. Morbi non magna. Nunc auctor nibh ac justo. Quisque egestas imperdiet risus. Nunc nibh ligula, imperdiet non, feugiat eu, commodo quis, justo. In hac habitasse platea dictumst. Aliquam in erat. Donec dignissim metus ac purus. Fusce velit.</p>
  </section>
  <div class="abs more" style="right:72px;top:844px">READ MORE</div>
  <div class="abs rule" style="left:352px;top:872px;width:776px"></div>

  <div class="abs photo" style="left:352px;top:900px;width:200px;height:200px" role="img" aria-label="Photo of two people in conversation at a networking table"></div>
  <section class="abs section" style="left:572px;top:904px;width:556px">
    <h2>SECTION B</h2>
    <h3>ArticleTitle</h3>
    <p>Lorem ipsum dolor sit amet, consectetuer adipiscing elit. Quisque egestas imperdiet risus. Nunc nibh ligula, imperdiet non, commodo quis, justo. In hac habitasse platea dictumst. Aliquam in erat. Donec dignissim metus ac purus. Fusce velit. Phasellus cursus.</p>
  </section>
  <div class="abs rule" style="left:352px;top:1132px;width:776px"></div>

  <section class="abs section" style="left:356px;top:1184px;width:396px">
    <h2>SECTION C</h2>
    <h3>ArticleTitle</h3>
    <p>Lorem ipsum dolor sit amet, consectetuer adipiscing elit. Duis pulvinar lectus. Fusce lacinia. Cras massa tortor, dignissim eu, sollicitudin eu, consequat et, magna. Proin tempor. Mauris leo orci, pretium at, ligula. Morbi non magna. Nunc auctor nibh ac justo.</p>
  </section>
  <div class="abs photo" style="left:768px;top:1188px;width:360px;height:272px" role="img" aria-label="Photo of guests in suits greeting each other at an evening reception"></div>
  <div class="abs more" style="left:664px;top:1440px">READ MORE</div>
  <div class="abs rule" style="left:352px;top:1480px;width:776px"></div>

  <section class="abs section" style="left:356px;top:1524px;width:396px">
    <h2>SECTION D</h2>
    <h3>ArticleTitle</h3>
    <p>Lorem ipsum dolor sit amet, consectetuer adipiscing elit. Duis pulvinar lectus. Fusce lacinia. Cras massa tortor, dignissim eu, sollicitudin eu, consequat et, magna. Proin tempor. Mauris leo orci, pretium at, ligula. Quisque egestas imperdiet risus. Aliquam sed mi non diam molestie posuere.</p>
  </section>
  <div class="abs photo" style="left:768px;top:1524px;width:360px;height:316px;background:linear-gradient(170deg,#6e5a3e,#c79a52 45%,#3d3326)" role="img" aria-label="Photo of a banquet hall with long tables under warm evening light"></div>
  <div class="abs more" style="left:664px;top:1834px">READ MORE</div>
</main>

<div class="abs events-band"></div>
<div class="abs side-head" style="top:1912px">EVENTS</div>
<ul class="abs event-list">
  <li><b>› Title</b><span>Year | Month | Day</span></li>
  <li><b>› Title</b><span>Year | Month | Day</span></li>
  <li><b>› Title</b><span>Year | Month | Day</span></li>
  <li><b>› Title</b><span>Year | Month | Day</span></li>
</ul>

<div class="abs photo" style="left:352px;top:1912px;width:320px;height:200px" role="img" aria-label="Photo of a crowded exhibition floor with visitors at stands"></div>
<section class="abs section" style="left:690px;top:1912px;width:438px">
  <h2>SECTION E</h2>
  <h3>ArticleTitle</h3>
  <p style="font-size:14px">Lorem ipsum dolor sit amet, consectetuer adipiscing elit. Quisque egestas imperdiet risus. Nunc nibh ligula, imperdiet non, commodo quis, justo. In hac habitasse platea dictumst. Donec dignissim metus. Fusce velit.</p>
</section>
<div class="abs more" style="right:72px;top:2128px">READ MORE</div>

<aside class="abs about">
  <h2>ABOUT KVRB</h2>
  <p>KVRB was formed to give the coach planning trade a shared voice. Since 1989, KVRB has represented its members in regional and national forums, delivering specialist events and practical training workshops.</p>
  <p style="margin-top:8px">KVRB Ltd, 14 Fjordgate Lane, Bergen | <b>REGISTRATION NUMBER</b> 4580271</p>
</aside>

<div class="abs more" style="left:218px;top:2300px">FIND MORE</div>

<footer>
  <div class="abs rule footer-rule"></div>
  <div class="abs copyright">COPYRIGHT © 2013 | All rights reserved</div>
  <div class="abs follow"><small>Follow us</small><div class="icons"><span></span><span></span><span></span><span></span><span></span></div></div>
</footer>

</body>
</html>
```